PowerPoint Design for Real Estate Investment Company
Verrick Holdings LLC
PowerPoint Design for Real Estate Investment Company - Real Estate
Creative Brief
Professional
P.O. Box 519 Corvell Springs, ST 00000
info@verrickholdings-example.com

```html
<!DOCTYPE html>
<html lang="en">
<head>
<meta charset="utf-8">
<title>Verrick Holdings LLC – Presentation Template</title>
<link href="https://fonts.googleapis.com/css2?family=Arimo:wght@400;700&family=PT+Sans:wght@400;700&family=Questrial&display=swap" rel="stylesheet">
<style>
:root{
  --backdrop:#9c9c9c;
  --navy:#0f3a6e;
  --navy-deep:#0a1a33;
  --navy-mid:#1b4f8c;
  --ink:#333;
  --grey-text:#555;
  --rule:#9a9a9a;
  --photo:#4a4a4a;
  --white:#fff;
}
*{margin:0;padding:0;box-sizing:border-box}
html,body{width:1200px;height:624px;overflow:hidden}
body{background:var(--backdrop);position:relative;font-family:"Arimo",Arial,sans-serif;color:var(--ink)}
.slide{position:absolute;width:336px;height:252px;background:var(--white);box-shadow:0 1px 4px rgba(0,0,0,.35);overflow:hidden}
.col1{left:77px}.col2{left:436px}.col3{left:796px}
.row1{top:54px}.row2{top:323px}

.accent{position:absolute;left:0;top:0;width:8px;height:100%;
  background:linear-gradient(to bottom,#9a9a9a 0%,#3a3a3a 24%,var(--navy-deep) 24.5%,#0b1f3e 60%,var(--navy-mid) 100%)}
.accent::after{content:"";position:absolute;left:-2px;top:60px;width:14px;height:1.5px;background:var(--white);transform:rotate(-40deg)}
.accent.wide{width:12px}
.accent.wide::after{top:98px;width:20px}

.head h2{position:absolute;left:18px;top:18px;font-family:"PT Sans",sans-serif;font-weight:700;font-size:14px;color:var(--navy);letter-spacing:.1px}
.head .sub{position:absolute;left:18px;top:35px;right:19px;display:flex;align-items:flex-end;gap:3px;font-family:"PT Sans",sans-serif;font-weight:700;font-size:7.5px;color:var(--grey-text)}
.head .sub::after{content:"";flex:1;height:1px;background:var(--rule);margin-bottom:2px}
.mark{position:absolute;right:20px;top:16px;display:flex;align-items:center;gap:3px}
.mark .sq{width:8px;height:8px;background:var(--navy)}
.mark span{font-family:"PT Sans",sans-serif;font-weight:700;font-size:6px;color:var(--navy);line-height:1}

.url{position:absolute;left:0;right:0;bottom:10px;text-align:center;font-size:5px;letter-spacing:.8px;color:var(--grey-text);font-style:italic}
.copy{font-size:4.6px;line-height:1.55;color:var(--ink)}

.brand{position:absolute;left:32px;top:30px;font-family:"PT Sans",sans-serif;font-weight:700;font-size:16px;line-height:1.05;color:var(--navy)}
.welcome{position:absolute;right:24px;top:170px;text-align:right;font-family:"Arimo",sans-serif}
.welcome .w1{font-size:16px;color:#555;letter-spacing:-.4px}
.welcome .w2{font-size:16.5px;font-weight:700;color:var(--navy);margin-top:2px}
.welcome .w3{font-size:15px;color:#555;margin-top:2px;letter-spacing:-.3px}

.team{position:absolute;top:74px;width:64px}
.team .photo{width:64px;height:64px;background:var(--photo);border:2px solid #e6e6e6;box-shadow:0 0 2px rgba(0,0,0,.4)}
.team h3{margin-top:20px;font-family:"PT Sans",sans-serif;font-weight:700;font-size:7px;color:var(--navy)}
.team .role{font-size:6px;font-style:italic;color:#777;margin-top:1px}
.team .copy{margin-top:5px;text-align:justify}

.group{position:absolute;width:145px}
.group h3{font-family:"PT Sans",sans-serif;font-weight:700;font-size:7.5px;color:var(--navy);margin-bottom:3px}
.group .copy{text-align:justify}

.bars{position:absolute;left:30px;top:62px}
.bar-note{position:absolute;left:204px;top:62px;width:92px}
.bar-note p+p{margin-top:5px}
.foot-copy{position:absolute;left:28px;top:186px;width:280px;text-align:justify}
.pie-text{position:absolute;left:26px;top:80px;width:140px;text-align:center}
.pie-text p+p{margin-top:7px}
.pie{position:absolute;left:206px;top:68px}
.legend{position:absolute;left:207px;top:160px;width:92px}
.legend li{list-style:none;display:flex;align-items:center;gap:4px;font-size:4.4px;padding:2px 0;border-bottom:1px solid #bbb}
.legend i{width:5px;height:5px;display:block}
.pie-foot{position:absolute;left:207px;top:187px;width:100px}

.closing{background:radial-gradient(ellipse at 52% 42%,#1f5593 0%,#123a6b 40%,var(--navy-deep) 85%)}
.closing h2{position:absolute;left:0;right:0;top:86px;text-align:center;font-family:"Questrial",sans-serif;font-weight:400;font-size:47px;color:var(--white);letter-spacing:-.5px}
.closing h3{position:absolute;left:0;right:0;top:136px;text-align:center;font-family:"Questrial",sans-serif;font-weight:400;font-size:26px;color:var(--white)}
.contact{position:absolute;left:0;right:0;top:224px;text-align:center;font-size:5px;line-height:1.7;color:#e6ecf5}
.contact b{font-weight:700}

.caption{position:absolute;left:0;right:0;top:585px;text-align:center;font-family:"Arimo",sans-serif;font-weight:700;font-size:14.5px;color:var(--white);text-shadow:0 0 2px #000,0 0 2px #000}
</style>
</head>
<body>

<section class="slide col1 row1 title-slide">
  <div class="accent wide"></div>
  <div class="brand">Verrick Holdings LLC</div>
  <div class="welcome">
    <div class="w1">WELCOME TO OUR</div>
    <div class="w2">PRESENTATION NAME</div>
    <div class="w3">DESCRIPTION</div>
  </div>
</section>

<section class="slide col2 row1 team-slide">
  <div class="accent"></div>
  <header class="head"><h2>Heading Here</h2><div class="sub">Sub Heading</div></header>
  <div class="mark"><div class="sq"></div><span>Verrick Holdings</span></div>
  <div class="team" style="left:26px"><div class="photo" role="img" aria-label="Team member photo"></div><h3>Team member1</h3><div class="role">Title</div><p class="copy">Lorem ipsum dolor sit amet, consectetur adipiscing elit, sed do eiusmod tempor incididunt</p></div>
  <div class="team" style="left:100px"><div class="photo" role="img" aria-label="Team member photo"></div><h3>Team member2</h3><div class="role">Title</div><p class="copy">ut labore et dolore magna aliqua. Ut enim ad minim veniam, quis nostrud exercitation</p></div>
  <div class="team" style="left:174px"><div class="photo" role="img" aria-label="Team member photo"></div><h3>Team member3</h3><div class="role">Title</div><p class="copy">ullamco laboris nisi ut aliquip ex ea commodo consequat. Enim ad minim veniam,</p></div>
  <div class="team" style="left:248px"><div class="photo" role="img" aria-label="Team member photo"></div><h3>Team member4</h3><div class="role">Title</div><p class="copy">Do eiusmod tempor incididunt. Lorem ipsum dolor sit amet, consectetur adipiscing elit, sed</p></div>
  <div class="url">www.verrickholdings-example.com</div>
</section>

<section class="slide col3 row1 groups-slide">
  <div class="accent"></div>
  <header class="head"><h2>Heading Here</h2><div class="sub">Sub Heading</div></header>
  <div class="mark"><div class="sq"></div><span>Verrick Holdings</span></div>
  <div class="group" style="left:20px;top:62px"><h3>Group1</h3><p class="copy">Lorem ipsum dolor sit amet, consectetur adipiscing elit, sed do eiusmod tempor incididunt ut labore et dolore magna aliqua. Ut enim ad minim veniam, quis nostrud exercitation ullamco laboris nisi ut aliquip ex ea commodo consequat.</p></div>
  <div class="group" style="left:173px;top:62px"><h3>Group4</h3><p class="copy">Lorem ipsum dolor sit amet, consectetur adipiscing elit, sed do eiusmod tempor incididunt ut labore et dolore magna aliqua. Ut enim ad minim veniam, quis nostrud exercitation ullamco laboris nisi ut aliquip ex ea commodo consequat.</p></div>
  <div class="group" style="left:18px;top:119px"><h3>Group2</h3><p class="copy">Duis aute irure dolor in reprehenderit in voluptate velit esse cillum dolore eu fugiat nulla pariatur. Excepteur sint occaecat cupidatat non proident, sunt in culpa qui officia deserunt mollit anim id est laborum.</p></div>
  <div class="group" style="left:173px;top:119px"><h3>Group5</h3><p class="copy">Duis aute irure dolor in reprehenderit in voluptate velit esse cillum dolore eu fugiat nulla pariatur. Excepteur sint occaecat cupidatat non proident, sunt in culpa qui officia deserunt mollit anim id est laborum.</p></div>
  <div class="group" style="left:19px;top:171px"><h3>Group3</h3><p class="copy">Duis aute irure dolor in reprehenderit in voluptate velit esse cillum dolore eu fugiat nulla pariatur. Excepteur sint occaecat cupidatat non proident, sunt in culpa qui officia deserunt mollit anim id est laborum.</p></div>
  <div class="group" style="left:172px;top:171px"><h3>Group6</h3><p class="copy">Duis aute irure dolor in reprehenderit in voluptate velit esse cillum dolore eu fugiat nulla pariatur. Excepteur sint occaecat cupidatat non proident, sunt in culpa qui officia deserunt mollit anim id est laborum.</p></div>
  <div class="url">www.verrickholdings-example.com</div>
</section>

<section class="slide col1 row2 bar-slide">
  <div class="accent"></div>
  <header class="head"><h2>Heading Here</h2><div class="sub">Sub Heading</div></header>
  <div class="mark"><div class="sq"></div><span>Verrick Holdings</span></div>
  <svg class="bars" width="136" height="104" viewBox="0 0 136 104" role="img" aria-label="Bar chart with four values">
    <defs><linearGradient id="barFill" x1="0" y1="0" x2="0" y2="1"><stop offset="0" stop-color="#16467f"/><stop offset="1" stop-color="#0a1c38"/></linearGradient></defs>
    <g stroke="#c8c8c8" stroke-width=".6">
      <line x1="2" y1="2" x2="134" y2="2"/><line x1="2" y1="9" x2="134" y2="9"/><line x1="2" y1="16" x2="134" y2="16"/><line x1="2" y1="23" x2="134" y2="23"/><line x1="2" y1="30" x2="134" y2="30"/><line x1="2" y1="37" x2="134" y2="37"/><line x1="2" y1="44" x2="134" y2="44"/><line x1="2" y1="51" x2="134" y2="51"/><line x1="2" y1="58" x2="134" y2="58"/><line x1="2" y1="65" x2="134" y2="65"/><line x1="2" y1="72" x2="134" y2="72"/><line x1="2" y1="79" x2="134" y2="79"/><line x1="2" y1="86" x2="134" y2="86"/><line x1="2" y1="93" x2="134" y2="93"/><line x1="2" y1="101" x2="134" y2="101"/>
    </g>
    <rect x="33" y="5" width="16" height="96" fill="url(#barFill)"/>
    <rect x="53" y="19" width="16" height="82" fill="url(#barFill)"/>
    <rect x="73" y="42" width="16" height="59" fill="url(#barFill)"/>
    <rect x="93" y="26" width="16" height="75" fill="url(#barFill)"/>
    <g fill="#fff" font-family="Arimo, sans-serif" font-size="5">
      <text transform="translate(43 98) rotate(-90)">Sub text1</text>
      <text transform="translate(63 98) rotate(-90)">Sub text2</text>
      <text transform="translate(83 98) rotate(-90)">Sub text3</text>
      <text transform="translate(103 98) rotate(-90)">Sub text4</text>
    </g>
  </svg>
  <div class="bar-note copy">
    <p>Lorem ipsum dolor sit amet, consectetur adipiscing elit, sed do eiusmod tempor incididunt ut labore et dolore magna aliqua. Ut enim ad minim veniam, quis nostrud.</p>
    <p>consectetur adipiscing elit, sed do eiusmod tempor incididunt ut labore. Lorem ipsum dolor sit amet, et dolore magna aliqua. Ut enim ad minim veniam, quis nostrud.</p>
  </div>
  <p class="foot-copy copy">Lorem ipsum dolor sit amet, consectetur adipiscing elit, sed do eiusmod tempor incididunt ut labore et dolore magna aliqua. Ut enim ad minim veniam, quis nostrud exercitation ullamco laboris nisi ut aliquip ex ea commodo consequat. Duis aute irure dolor in reprehenderit in voluptate velit esse cillum dolore eu fugiat nulla pariatur. Excepteur sint occaecat cupidatat non proident, sunt in culpa qui officia deserunt mollit anim id est laborum.</p>
  <div class="url">www.verrickholdings-example.com</div>
</section>

<section class="slide col2 row2 pie-slide">
  <div class="accent"></div>
  <header class="head"><h2>Heading Here</h2><div class="sub">Sub Heading</div></header>
  <div class="mark"><div class="sq"></div><span>Verrick Holdings</span></div>
  <div class="pie-text copy">
    <p>Lorem ipsum dolor sit amet, consectetur adipiscing elit, sed do eiusmod tempor incididunt ut labore et dolore magna aliqua. Ut enim ad minim veniam, quis nostrud exercitation ullamco laboris nisi ut aliquip ex ea commodo consequat. Duis aute irure dolor in reprehenderit in voluptate velit esse cillum dolore eu fugiat nulla pariatur. Excepteur sint occaecat cupidatat non proident, sunt in culpa qui officia deserunt mollit anim id est laborum.</p>
    <p>Excepteur sint occaecat cupidatat non proident, sunt in culpa qui officia deserunt mollit anim id est laborum. Ut enim ad minim veniam, quis nostrud exercitation ullamco laboris nisi ut aliquip ex ea commodo consequat.</p>
  </div>
  <svg class="pie" width="80" height="80" viewBox="-40 -40 80 80" role="img" aria-label="Pie chart split into four parts">
    <defs><radialGradient id="pieNavy" cx="0.4" cy="0.4" r="0.7"><stop offset="0" stop-color="#1d5191"/><stop offset="1" stop-color="#0a1a33"/></radialGradient></defs>
    <g stroke="#fff" stroke-width=".8">
      <path d="M0 0 L0 -37 A37 37 0 0 1 30.3 -21.2 Z" fill="#575757"/>
      <path d="M0 0 L30.3 -21.2 A37 37 0 0 1 36.4 6.4 Z" fill="url(#pieNavy)"/>
      <path d="M0 0 L36.4 6.4 A37 37 0 0 1 18.5 32 Z" fill="#575757"/>
      <path d="M0 0 L18.5 32 A37 37 0 1 1 0 -37 Z" fill="url(#pieNavy)"/>
    </g>
  </svg>
  <ul class="legend">
    <li><i style="background:var(--navy-deep)"></i>Lorem ipsum dolor sit amet 50%</li>
    <li><i style="background:#575757"></i>Duis aute irure dolor in 50%</li>
  </ul>
  <p class="pie-foot copy">sunt in culpa qui officia deserunt mollit anim id est laborum. Ut enim ad minim veniam</p>
  <div class="url">www.verrickholdings-example.com</div>
</section>

<section class="slide col3 row2 closing">
  <h2>Thanks</h2>
  <h3>For Coming</h3>
  <div class="contact">
    P.O. Box 519, Corvell Springs, ST 00000 &nbsp;| &nbsp;<b>P :</b> 555 010 2233 &nbsp;<b>C :</b> 555 010 4455<br>
    <b>F :</b> 555 010 4455 &nbsp;<b>E :</b> info@verrickholdings-example.com &nbsp;<b>W :</b> www.verrickholdings-example.com
  </div>
</section>

<div class="caption">Power point template</div>

</body>
</html>
```